Design our branded business card!

We'd love for you to design our business card and come up with a fitting design that reflects the Pivex brand. We're a growing tech startup with big ambitions. We've included our brand guidelines (contain colour palette), logo (EPS vector in CMYK) and old designs to help you on your way.

We'd like to keep the design fairly simple:

* Name
* Phone number
* Email address
* Website (www.pivex.life)
* Twitter (@pivex)
* Address (18 Wexham Row, Leeds, UK, LS9 4ZQ).

This would need to include print and cutting marks.

If you have any questions just let us know!

Target Market(s)

Businesses, Press and our customers!

Industry/Entity Type

Business

Contact Information for Business Card

* Name
* Phone number
* Email address
* Twitter (@pivex)

Font styles to use
Sans Serif

Requirements
Must have
• 1. Must have the Pivex logo included.
• 2. Must use the font 'Brandon Text' in either 'light' or 'thin' (https://www.typevault-demo.com/fonts/qrsfonts/halden-sans/)
• 3. Must use exact colours references from the brand guidelines. Colours outside of the brand guidelines will be discounted. White (transparent) backgrounds are fine.
• 4. Must contain the following information:
• * Name
• * Phone number
• * Email address
• * Website (www.pivex.life)
• * Twitter (@pivex)
• * Address (18 Wexham Row, Leeds, UK, LS9 4ZQ).
Nice to have
• Must use the font 'Brandon Text' in either 'light' or 'thin' (https://www.typevault-demo.com/fonts/qrsfonts/halden-sans/)
Should not have
• Colours outside of the brand guidelines will be discounted. White (transparent) backgrounds are fine.
• Avoid creating icons or including photography.

```html
<!DOCTYPE html>
<html lang="en">
<head>
<meta charset="utf-8">
<title>Pivex business card</title>
<link rel="stylesheet" href="https://fonts.googleapis.com/css2?family=Josefin+Sans:wght@300;400&display=swap">
<style>
  :root {
    --brand-green: #7dc474;
    --ink: #333535;
    --paper: #ffffff;
    --backdrop: #e9e9e7;
    --card-w: 500px;
    --card-h: 286px;
  }
  * { box-sizing: border-box; margin: 0; padding: 0; }
  html, body { width: 1200px; height: 800px; overflow: hidden; }
  body {
    background: var(--backdrop);
    font-family: "Josefin Sans", sans-serif;
    font-weight: 300;
    color: var(--ink);
    position: relative;
  }
  .card {
    position: absolute;
    top: 257px;
    width: var(--card-w);
    height: var(--card-h);
    overflow: hidden;
    box-shadow: 0 4px 14px rgba(0,0,0,0.12);
  }
  .card--front { left: 70px; background: var(--paper); }
  .card--back { left: 630px; background: var(--brand-green); }

  .wordmark {
    position: absolute;
    display: flex;
    align-items: center;
    gap: 12px;
  }
  .wordmark__dot { border-radius: 50%; flex: none; }
  .wordmark__name { font-weight: 300; line-height: 1; letter-spacing: 1px; }

  .card--front .wordmark { top: 52px; right: 34px; }
  .card--front .wordmark__dot { width: 56px; height: 56px; background: var(--brand-green); }
  .card--front .wordmark__name { font-size: 54px; color: var(--ink); padding-top: 8px; }

  .holder-name { position: absolute; left: 16px; top: 148px; font-size: 20px; }

  .band { position: absolute; left: 0; width: 100%; }
  .band--green { background: var(--brand-green); color: var(--paper); }
  .band--1 { top: 170px; height: 22px; }
  .band--2 { top: 214px; height: 22px; }
  .band--3 { top: 258px; height: 14px; }

  .detail {
    position: absolute;
    display: flex;
    align-items: center;
    gap: 8px;
    font-size: 12px;
    letter-spacing: 0.3px;
    line-height: 1;
  }
  .detail svg { width: 14px; height: 14px; flex: none; }
  .detail--twitter { left: 300px; top: 174px; color: var(--paper); }
  .detail--address { left: 16px; top: 197px; }
  .detail--web { left: 300px; top: 196px; }
  .detail--phone { left: 16px; top: 218px; color: var(--paper); }
  .detail--email { left: 16px; top: 240px; }

  .card--back .wordmark { top: 100px; left: 110px; }
  .card--back .wordmark__dot { width: 70px; height: 70px; background: var(--paper); }
  .card--back .wordmark__name { font-size: 60px; color: var(--paper); padding-top: 10px; }

  .back-corner { position: absolute; top: 0; right: 0; width: 26px; height: 14px; background: var(--paper); }
  .back-strip {
    position: absolute; left: 0; top: 226px; width: 100%; height: 26px;
    background: var(--paper);
    display: flex; align-items: center; padding-left: 40px;
    font-size: 13px; letter-spacing: 6px; color: var(--ink);
  }
</style>
</head>
<body>

<section class="card card--front" aria-label="Business card front">
  <div class="wordmark">
    <span class="wordmark__dot"></span>
    <span class="wordmark__name">pivex</span>
  </div>

  <p class="holder-name">Name</p>

  <div class="band band--green band--1"></div>
  <div class="band band--green band--2"></div>
  <div class="band band--green band--3"></div>

  <p class="detail detail--twitter">
    <svg viewBox="0 0 14 14"><circle cx="7" cy="7" r="6" fill="currentColor"/></svg>
    @pivex
  </p>
  <p class="detail detail--address">18 Wexham Row, Leeds, UK, LS9 4ZQ</p>
  <p class="detail detail--web">
    <svg viewBox="0 0 14 14" fill="none" stroke="currentColor" stroke-width="1">
      <circle cx="7" cy="7" r="6"/><ellipse cx="7" cy="7" rx="2.6" ry="6"/><path d="M1 7h12M2 4h10M2 10h10"/>
    </svg>
    www.pivex.life
  </p>
  <p class="detail detail--phone">
    <svg viewBox="0 0 14 14" fill="currentColor">
      <path d="M1 5c0-2 2-3 6-3s6 1 6 3v1h-3V4.5H4V6H1z"/><rect x="3" y="7" width="8" height="6" rx="1"/>
    </svg>
    111-1111-1111
  </p>
  <p class="detail detail--email">
    <svg viewBox="0 0 14 14" fill="none" stroke="currentColor" stroke-width="1">
      <rect x="1" y="3" width="12" height="8"/><path d="M1 3l6 5 6-5M1 11l4.5-4M13 11l-4.5-4"/>
    </svg>
    email@email.com
  </p>
</section>

<section class="card card--back" aria-label="Business card back">
  <div class="back-corner"></div>
  <div class="wordmark">
    <span class="wordmark__dot"></span>
    <span class="wordmark__name">pivex</span>
  </div>
  <p class="back-strip">www.pivex.life</p>
</section>

</body>
</html>
```